PressKit website design for Tavi Linkway-Africa

We need a website for a new consultancy and digital marketplace in Kenya called 'Tavi Linkway - Africa'. Please refer to the the attached document [Tavi Linkway Africa website brief] and contact me anytime.

Bests,
Philippa

Deadline extended to allow for additional revisions and refinements, ensuring that final designs align closely with project objectives and quality standards. This extra time will help incorporate valuable feedback and ensure the final output meets our high expectations.

```html
<!DOCTYPE html>
<html lang="en">
<head>
<meta charset="utf-8">
<title>Tavi Linkway Africa</title>
<link rel="stylesheet" href="https://fonts.googleapis.com/css2?family=Poppins:wght@300;400;500;600;700&display=swap">
<style>
:root{
  --blue:#1463ff;
  --blue-soft:#2b7bff;
  --navy:#1f2a96;
  --green:#8fd300;
  --green-dark:#5aa800;
  --ink:#1b1d22;
  --text:#4a4f5a;
  --muted:#8a8f99;
  --line:#e6e9ef;
  --pale:#eef3fa;
  --stage:#e9eaed;
  --black:#060607;
}
*{margin:0;padding:0;box-sizing:border-box}
html,body{width:1200px;height:3562px;overflow:hidden}
body{background:var(--stage);font-family:"Poppins",sans-serif;color:var(--ink);position:relative}
.page{position:absolute;left:133px;top:80px;width:974px;height:3482px;background:#fff;overflow:hidden}
.abs{position:absolute}
.eyebrow{font-size:7px;font-weight:600;letter-spacing:.3px;text-transform:uppercase;color:var(--blue)}
.h2{font-size:17px;font-weight:400;color:var(--ink)}
.h2 b{font-weight:600}
.small{font-size:7px;line-height:12px;color:var(--muted)}
.btn{position:absolute;display:flex;align-items:center;justify-content:center;font-size:7px;font-weight:500;color:#fff;border-radius:2px}

.topbar{left:0;top:0;width:974px;height:19px;background:linear-gradient(90deg,#1946ff,#1fa0ff)}
.topbar .msg{left:232px;top:5px;font-size:6.5px;color:#fff;font-weight:500}
.topbar .tag{left:196px;top:0;width:30px;height:19px;background:#0d2ed8}
.dot-s{width:7px;height:7px;border-radius:50%;background:#fff;opacity:.85;top:6px}

.logo{display:flex;align-items:center;gap:4px;font-weight:700;color:var(--ink)}
.logo i{display:block;border-radius:50%;background:var(--blue)}
.nav{left:276px;top:41px;display:flex;gap:24px;font-size:6.5px;font-weight:500;color:var(--ink)}
.hotline{left:549px;top:34px;display:flex;gap:6px;align-items:center}
.hotline .ic{width:20px;height:20px;border-radius:50%;background:var(--blue)}
.hotline small{display:block;font-size:5.5px;color:var(--muted)}
.hotline b{font-size:7.5px;font-weight:600}

.hero-title{left:254px;top:140px;font-size:25px;line-height:28px;font-weight:600}
.hero-sub{left:254px;top:197px;font-size:16px;line-height:17px;font-weight:400}
.hero-p{left:254px;top:240px;width:235px;font-size:7.5px;line-height:13px;color:var(--muted)}
.photo{left:524px;top:119px;width:226px;height:226px;border-radius:50%;background:radial-gradient(circle at 45% 40%,#d8dde3,#7c8591 60%,#3b3f48);box-shadow:-10px 8px 0 0 var(--blue)}

.statbox{left:196px;top:410px;width:590px;height:435px;background:linear-gradient(115deg,#1d2b9e 0%,#24459a 30%,#4e8f56 62%,#8ed400 100%);color:#fff}
.partners{top:41px;left:0;width:590px;font-size:11px;font-weight:600}
.partners span{position:absolute;white-space:nowrap;display:flex;align-items:center;gap:4px}
.partners i{width:9px;height:9px;background:#fff;border-radius:50%}
.quote{left:69px;top:112px;width:160px;font-size:12.5px;line-height:17px;font-weight:600}
.sig{left:69px;top:214px;font-size:5.5px;font-weight:600;letter-spacing:.4px}
.about{left:284px;top:112px;width:230px;font-size:6.6px;line-height:11.6px;font-weight:500}
.about p+p{margin-top:8px}
.statbox .btn{left:284px;top:300px;width:72px;height:20px;border:1px solid rgba(255,255,255,.8);font-size:6px}
.stat{top:371px;display:flex;align-items:center;gap:7px}
.stat b{font-size:17px;font-weight:600}
.stat small{font-size:5.5px;line-height:8px;text-transform:uppercase}

.card{position:absolute;width:185px;height:146px;background:#fff;border:1px solid var(--line);box-shadow:0 2px 6px rgba(20,40,80,.05);padding:16px}
.card h3{font-size:9.5px;font-weight:600}
.card .num{position:absolute;right:16px;top:17px;font-size:6.5px;color:var(--green-dark)}
.card svg{position:absolute;left:16px;top:48px}
.card p{position:absolute;left:16px;top:98px;width:150px;font-size:6.5px;line-height:12px;color:var(--muted)}

.map{left:0;top:1320px;width:337px;height:362px;border-radius:46% 54% 42% 58% / 38% 40% 60% 62%;background:radial-gradient(circle at 55% 35%,#3d7fe0,#283f9c 70%)}
.ring{border:1px solid #e3e7ef;border-radius:50%}
.why-list{left:546px;top:1458px;font-size:7.5px;font-weight:600;color:#24305e}
.why-list li{list-style:none;display:flex;align-items:center;gap:8px;height:32px}
.why-list li i{width:9px;height:9px;border-radius:50%;background:var(--blue)}

.market{left:0;top:1699px;width:974px;height:439px;background:var(--pale)}
.prod{position:absolute;top:114px;width:185px;height:238px;background:#fff}
.prod .shot{height:124px;background:linear-gradient(135deg,#1b5cff,#4c8dff)}
.prod h3{font-size:9.5px;font-weight:600;margin:10px 16px 0}
.prod .cat{font-size:5.5px;color:var(--green-dark);margin:3px 16px 0}
.prod p{font-size:6.5px;line-height:11px;color:var(--muted);margin:9px 16px 0;width:150px}
.tags{display:flex;gap:5px;margin:10px 16px 0}
.tags span{font-size:5.5px;background:var(--pale);color:var(--text);padding:2px 6px}
.arrow{width:16px;height:18px;display:flex;align-items:center;justify-content:center}
.pager{display:flex;gap:6px}
.pager i{width:4px;height:4px;border-radius:50%;background:#c3c9d3}

.member{position:absolute;width:120px;text-align:center}
.member .av{width:68px;height:68px;margin:0 auto;border-radius:50%;background:radial-gradient(circle at 50% 35%,#c8ccd3,#6f7682)}
.member h4{font-size:8.5px;font-weight:600;margin-top:12px}
.member small{display:block;font-size:6px;color:var(--muted);margin-top:2px}
.soc{display:flex;justify-content:center;gap:9px;margin-top:9px}
.soc i{width:8px;height:8px;border-radius:50%;border:1px solid #9aa2b1}

.post{position:absolute;top:2562px;width:148px;height:180px;color:#fff;padding:12px}
.post .label{font-size:5px;background:var(--green);display:inline-block;padding:2px 5px;font-weight:600}
.post h4{position:absolute;left:12px;top:130px;width:120px;font-size:8.5px;line-height:11px;font-weight:600}
.post .meta{position:absolute;left:12px;top:160px;font-size:5.5px;display:flex;gap:10px}

.contact{left:0;top:2801px;width:974px;height:364px;background:linear-gradient(90deg,#4f9e14,#7bc70a 60%,#95d800)}
.contact .info{left:252px;top:92px;color:#fff;font-size:6.5px;line-height:11px;width:240px}
.field{position:absolute;background:#fff;font-size:6px;color:var(--muted);padding:5px 6px}

.footer{left:0;top:3165px;width:974px;height:317px;background:var(--black);color:#fff}
.fcol{position:absolute;top:63px;font-size:6.5px;color:#9aa0aa;line-height:17px}
.fcol h5{font-size:8.5px;font-weight:600;color:#fff;line-height:14px;margin-bottom:4px}
.fcol .hl{font-size:8px;font-weight:600;color:#fff}
</style>
</head>
<body>
<div class="page">

  <div class="abs topbar">
    <div class="abs tag"></div>
    <div class="abs msg">Join us: Let's revolutionize Africa's <span style="opacity:.7">digital future</span></div>
    <span class="abs dot-s" style="left:678px"></span>
    <span class="abs dot-s" style="left:693px"></span>
    <span class="abs dot-s" style="left:708px"></span>
    <span class="abs dot-s" style="left:723px"></span>
  </div>

  <div class="abs logo" style="left:196px;top:36px;font-size:12px"><i style="width:12px;height:12px"></i>Tavi</div>
  <nav class="abs nav"><span>Home</span><span>Services</span><span>Shop</span><span>About</span><span>Blog</span><span>Contact</span></nav>
  <div class="abs hotline"><span class="ic"></span><div><small>Hotline 24/7</small><b>(+254) 700 555 010</b></div></div>
  <svg class="abs" style="left:678px;top:40px" width="10" height="10" viewBox="0 0 10 10"><circle cx="4" cy="4" r="3" fill="none" stroke="#1b1d22" stroke-width="1.1"/><path d="M6.3 6.3 9 9" stroke="#1b1d22" stroke-width="1.1"/></svg>
  <div class="btn" style="left:698px;top:36px;width:63px;height:19px;background:var(--blue);font-size:6px">Marketplace</div>

  <div class="abs" style="left:254px;top:125px;font-size:6px;font-weight:600;color:var(--green-dark)">TAVI LINKWAY AFRICA</div>
  <h1 class="abs hero-title">Empowering<br>Innovations</h1>
  <div class="abs hero-sub">&amp; Digital Transformation<br>Across Africa."</div>
  <p class="abs hero-p">We provide data-driven insights, strategic guidance, customised solutions to empower public and private sectors</p>
  <div class="btn" style="left:254px;top:316px;width:70px;height:22px;background:var(--ink)">our services</div>
  <div class="abs" style="left:340px;top:317px;width:20px;height:20px;border-radius:50%;background:var(--green)"></div>
  <div class="abs" style="left:367px;top:318px;font-size:5.5px;line-height:8px;color:var(--green-dark);font-weight:600">Intro<br>Reel</div>
  <div class="abs photo" role="img" aria-label="Photo of a team of young professionals gathered around a laptop"></div>

  <section class="abs statbox">
    <div class="abs partners">
      <span style="left:62px"><i></i>Newsdesk</span>
      <span style="left:166px"><i></i>Brightline</span>
      <span style="left:262px"><i></i>Byte Journal</span>
      <span style="left:378px"><i></i>Veltrix</span>
      <span style="left:470px"><i></i>Orbano</span>
    </div>
    <div class="abs quote">“We don’t just drive digital change; we make digital transformation work for Africa, one solution at a time.”</div>
    <div class="abs sig">PHILIPPA</div>
    <div class="abs about">
      <p>Tavi Linkway Africa is a consultancy firm and digital marketplace dedicated to supporting Africa's digital transformation. We provide data-driven insights, strategic guidance, customised solutions to empower public and private sectors. We aim to tackle complex challenges, optimize operations, and unlock growth through innovative technology.</p>
      <p>Our marketplace offers a curated selection of digital products and tools designed to support strategic growth, expand knowledge, strengthen data capabilities, and streamline operations. With deep expertise in digital transformation and a focus on Africa's unique opportunities, Tavi Linkway Africa is your trusted partner in navigating today's dynamic digital landscape. Together, we're advancing Africa's digital future.</p>
    </div>
    <div class="btn">More About Us</div>
    <div class="abs stat" style="left:70px"><b>20 +</b><small>Years of<br>experience</small></div>
    <div class="abs stat" style="left:187px"><b>15 K</b><small>Projects<br>completed</small></div>
    <div class="abs stat" style="left:305px"><b>240</b><small>Companies<br>impacted</small></div>
    <div class="abs stat" style="left:422px"><b>180</b><small>Satisfied clients<br>on 24 countries</small></div>
  </section>

  <div class="abs eyebrow" style="left:260px;top:904px">Our Services</div>
  <h2 class="abs h2" style="left:260px;top:923px"><b>Digital IT Solutions</b> For You</h2>

  <div class="card" style="left:202px;top:963px"><h3>Technical Expertise</h3><span class="num">01</span>
    <svg width="30" height="26" viewBox="0 0 30 26"><path d="M15 2 28 9 15 16 2 9Z" fill="#1463ff"/><path d="M2 15 15 22 28 15" fill="none" stroke="#5ea1ff" stroke-width="3"/></svg>
    <p>Trust our top minds to eliminate workflow pain points, implement new tech &amp; app.</p></div>
  <div class="card" style="left:398px;top:963px"><h3>Digital Strategy</h3><span class="num">02</span>
    <svg width="30" height="28" viewBox="0 0 30 28"><rect x="2" y="2" width="14" height="8" fill="#5ea1ff"/><circle cx="17" cy="13" r="4" fill="#1463ff"/><path d="M9 27c0-6 4-9 8-9s8 3 8 9Z" fill="#1463ff"/></svg>
    <p>Trust our top minds to eliminate workflow pain points, implement new tech &amp; app.</p></div>
  <div class="card" style="left:595px;top:963px"><h3>Analytics</h3><span class="num">03</span>
    <svg width="34" height="22" viewBox="0 0 34 22"><path d="M8 21a7 7 0 0 1 0-14 10 10 0 0 1 19 3 5.5 5.5 0 0 1 0 11Z" fill="#2b7bff"/></svg>
    <p>Trust our top minds to eliminate workflow pain points, implement new tech &amp; app.</p></div>
  <div class="card" style="left:202px;top:1122px"><h3>Advisory Solutions</h3><span class="num">04</span>
    <svg width="30" height="28" viewBox="0 0 30 28"><rect x="2" y="2" width="14" height="8" fill="#5ea1ff"/><circle cx="17" cy="13" r="4" fill="#1463ff"/><path d="M9 27c0-6 4-9 8-9s8 3 8 9Z" fill="#1463ff"/></svg>
    <p>Trust our top minds to eliminate workflow pain points, implement new tech &amp; app.</p></div>
  <div class="card" style="left:595px;top:1122px"><h3>E-commerce</h3><span class="num">05</span>
    <svg width="30" height="28" viewBox="0 0 30 28"><rect x="1" y="1" width="28" height="26" fill="#1463ff"/><rect x="4" y="8" width="22" height="6" fill="#9cc3ff"/><rect x="4" y="17" width="14" height="3" fill="#fff"/></svg>
    <p>Trust our top minds to eliminate workflow pain points, implement new tech &amp; app.</p></div>

  <div class="abs ring" style="left:80px;top:1360px;width:330px;height:330px"></div>
  <div class="abs ring" style="left:140px;top:1420px;width:210px;height:210px"></div>
  <div class="abs map" role="img" aria-label="Map of Africa made of glowing blue network dots"></div>
  <div class="abs" style="left:-20px;top:1577px;width:55px;height:55px;border-radius:50%;background:var(--blue)"></div>
  <div class="abs" style="left:98px;top:1520px;width:5px;height:5px;border-radius:50%;background:var(--ink)"></div>
  <div class="abs" style="left:362px;top:1512px;width:5px;height:5px;border-radius:50%;background:var(--ink)"></div>
  <div class="abs" style="left:31px;top:1653px;width:7px;height:7px;border-radius:50%;background:#888"></div>

  <div class="abs" style="left:546px;top:1329px;font-size:6px;font-weight:500;color:var(--blue)">Why Tavi Linkway Africa</div>
  <div class="abs" style="left:546px;top:1347px;font-size:16px;line-height:24px"><b style="font-weight:600">Empowering Africa's</b><br>Digital transformation</div>
  <p class="abs small" style="left:546px;top:1414px;width:215px;line-height:14px">We don't just drive digital change; we make digital transformation work for Africa, one solution at a time.</p>
  <ul class="abs why-list">
    <li><i></i>Innovation and new tech</li>
    <li><i></i>Customer-centric approach</li>
    <li><i></i>Passion driven solutions</li>
    <li><i></i>Eco-conscious approach</li>
  </ul>
  <div class="btn" style="left:546px;top:1620px;width:82px;height:24px;background:var(--blue)">How We Work</div>

  <section class="abs market">
    <div class="abs eyebrow" style="left:251px;top:61px">Featured Solutions</div>
    <h2 class="abs h2" style="left:251px;top:80px"><b>Explore</b> Our Marketplace</h2>
    <div class="prod" style="left:202px"><div class="shot" role="img" aria-label="Screenshots of a fleet rental dashboard template"></div>
      <h3>Fleet Rental Dashboard</h3><div class="cat">TECH , LANDING PAGE , UI/UX DESIGN</div>
      <p>Trust our top minds to eliminate workflow pain points, implement new tech &amp; app.</p>
      <div class="tags"><span>Plugin</span><span>Theme</span><span>PressKit</span></div></div>
    <div class="prod" style="left:398px"><div class="shot" role="img" aria-label="Mock-up of a landing page on phone and desktop"></div>
      <h3>Creative Landing Page</h3><div class="cat">TECH , UI/UX DESIGN</div>
      <p>Trust our top minds to eliminate workflow pain points, implement new tech &amp; app.</p>
      <div class="tags"><span>Framekit</span><span>PressKit</span></div></div>
    <div class="prod" style="left:595px"><div class="shot" role="img" aria-label="Mock-up of a landing page on phone and desktop"></div>
      <h3>Creative Landing Page</h3><div class="cat">TECH , UI/UX DESIGN</div>
      <p>Trust our top minds to eliminate workflow pain points, implement new tech &amp; app.</p>
      <div class="tags"><span>Framekit</span><span>PressKit</span></div></div>
    <div class="abs arrow" style="left:169px;top:309px;background:var(--green-dark)"><svg width="6" height="8"><path d="M5 1 1 4 5 7" fill="none" stroke="#fff" stroke-width="1.3"/></svg></div>
    <div class="abs arrow" style="left:799px;top:309px;background:#fff"><svg width="6" height="8"><path d="M1 1 5 4 1 7" fill="none" stroke="#5aa800" stroke-width="1.3"/></svg></div>
    <div class="abs pager" style="left:457px;top:384px"><i></i><i></i><i></i><i style="background:#444"></i><i></i><i></i><i></i><i></i></div>
  </section>

  <div class="abs eyebrow" style="left:0;width:974px;text-align:center;top:2146px">Meet Our Experts</div>
  <h2 class="abs h2" style="left:0;width:974px;text-align:center;top:2163px"><b>The Team</b> Empowering digital transformation</h2>
  <div class="member" style="left:196px;top:2205px"><div class="av" role="img" aria-label="Portrait of the CEO"></div><h4>Otieno Baraka</h4><small>CEO Founder</small><div class="soc"><i></i><i></i><i></i><i></i></div></div>
  <div class="member" style="left:313px;top:2205px"><div class="av" role="img" aria-label="Portrait of the CTO"></div><h4>Wanjiru Amani</h4><small>CTO</small><div class="soc"><i></i><i></i><i></i></div></div>
  <div class="member" style="left:431px;top:2205px"><div class="av" role="img" aria-label="Portrait of the project manager"></div><h4>Daniel Kiprono</h4><small>Project Manager</small><div class="soc"><i></i><i></i><i></i><i></i></div></div>
  <div class="member" style="left:549px;top:2205px"><div class="av" role="img" aria-label="Portrait of the marketing leader"></div><h4>Njeri Chelimo</h4><small>Marketing Leader</small><div class="soc"><i></i><i></i></div></div>
  <div class="member" style="left:667px;top:2205px"><div class="av" role="img" aria-label="Portrait of the creative director"></div><h4>Samuel Ouma</h4><small>Creative Director</small><div class="soc"><i></i><i></i><i></i></div></div>
  <div class="btn" style="left:419px;top:2365px;width:57px;height:22px;background:var(--ink)">About Us</div>
  <div class="btn" style="left:483px;top:2365px;width:79px;height:22px;background:var(--blue)">Join Our Team</div>

  <div class="abs eyebrow" style="left:255px;top:2510px;color:var(--green-dark)">Blog</div>
  <h2 class="abs h2" style="left:255px;top:2526px"><b>Latest Posts</b> From Our Blog</h2>
  <div class="abs" style="left:685px;top:2527px;font-size:10px;color:#ccc">‹ <span style="color:var(--green-dark)">›</span></div>
  <article class="post" style="left:202px;background:linear-gradient(160deg,#f0a640,#d0406a 55%,#2a2f55)" role="img" aria-label="Phone with colourful app icons"><span class="label">TIPS &amp; TRICKS</span><h4>Tips To Help You Build Your Social</h4><div class="meta"><span>By admin</span><span>May 4, 2022</span></div></article>
  <article class="post" style="left:350px;background:linear-gradient(160deg,#1e3a4a,#0d1820 60%,#111)" role="img" aria-label="Glowing video app icon on a dark background"><span class="label">TIPS &amp; TRICKS</span><h4>Clipstream New Trend Of Marketing</h4><div class="meta"><span>By admin</span><span>May 4, 2022</span></div></article>
  <article class="post" style="left:498px;background:linear-gradient(160deg,#9aa2ae,#4b5260 60%,#23262d)" role="img" aria-label="Freelancers working on laptops in a shared office"><span class="label">TIPS &amp; TRICKS</span><h4>Freelancer Days 2022, What's new?</h4><div class="meta"><span>By admin</span><span>May 4, 2022</span></div></article>
  <article class="post" style="left:646px;background:linear-gradient(160deg,#e6e6e4,#a9a8a2 60%,#5b5a55)" role="img" aria-label="Man writing a strategy plan on a whiteboard"><span class="label">TIPS &amp; TRICKS</span><h4>Workflow Strategy For E-Shop</h4><div class="meta"><span>By admin</span><span>May 4, 2022</span></div></article>

  <section class="abs contact">
    <div class="abs" style="left:0;width:974px;text-align:center;top:58px;font-size:6px;font-weight:600;color:#fff">CONTACT US</div>
    <div class="abs" style="left:0;width:974px;text-align:center;top:72px;font-size:15px;color:#fff"><b style="font-weight:600">Request Free</b> Consultancy</div>
    <div class="abs info">
      <div style="font-size:5.5px">Hotline 24/7</div>
      <div style="font-size:9px;font-weight:600">(+254) 700 555 010</div>
      <div style="margin-top:16px"><b>Address :</b> Mara Lane, Kileleshwa, Nairobi Kenya, Off Ridge road.</div>
      <div style="margin-top:10px"><b>Email :</b> contact@tavilinkway.example</div>
      <div style="margin-top:10px"><b>Work Hours :</b> Mon - Sat: 9:00 - 18:00</div>
      <div style="margin-top:34px;text-decoration:underline;font-weight:600">GET DIRECTION</div>
    </div>
    <div class="field" style="left:496px;top:102px;width:110px;height:22px">Name</div>
    <div class="field" style="left:622px;top:102px;width:111px;height:22px">Email</div>
    <div class="field" style="left:496px;top:133px;width:237px;height:22px;display:flex;justify-content:space-between">Your inquiry about <span>⌄</span></div>
    <div class="field" style="left:496px;top:164px;width:237px;height:70px">Message</div>
    <div class="abs" style="left:496px;top:243px;font-size:5.5px;color:#fff;display:flex;gap:4px;align-items:center"><i style="width:6px;height:6px;background:#fff;display:block"></i>By submitting, I'm agreed to the Terms &amp; Conditions</div>
    <div class="btn" style="left:496px;top:266px;width:78px;height:22px;background:var(--ink)">Send Message</div>
  </section>

  <footer class="abs footer">
    <div class="abs" style="left:202px;top:56px">
      <div class="logo" style="font-size:25px;color:#fff"><i style="width:22px;height:22px"></i>Tavi</div>
      <div style="font-size:6.5px;color:#9aa0aa;margin:2px 0 0 30px;letter-spacing:.5px">LINKWAY AFRICA</div>
      <div style="font-size:6px;font-weight:600;margin-top:14px;line-height:10px;width:170px">Empowering Innovations &amp; Digital Transformation Across Africa</div>
      <div style="font-size:6px;color:#9aa0aa;line-height:14px;margin-top:10px">Mara Lane, Kileleshwa, Nairobi Kenya<br>contact@tavilinkway.example<br>+254 700 555 010</div>
      <div style="display:flex;gap:6px;margin-top:12px"><i style="width:16px;height:16px;border-radius:50%;background:#2b2d33;display:block"></i><i style="width:16px;height:16px;border-radius:50%;background:#2b2d33;display:block"></i><i style="width:16px;height:16px;border-radius:50%;background:#2b2d33;display:block"></i><i style="width:16px;height:16px;border-radius:50%;background:#2b2d33;display:block"></i><i style="width:16px;height:16px;border-radius:50%;background:#2b2d33;display:block"></i></div>
    </div>
    <div class="fcol" style="left:379px"><h5>Services</h5>Digital Strategy<br>Technical Expertise<br>Data Analytics<br>Artificial Intelligence<br><span class="hl">Digital Marketplace</span><br>Templates<br>Guides<br>Courses</div>
    <div class="fcol" style="left:496px"><h5>Information</h5>About Us<br>Contact<br>Marketplace<br>How It Works<br>Pricing Plan</div>
    <div class="fcol" style="left:615px;width:200px;line-height:13px"><h5>Newsletter</h5>Register now to get latest updates on promotions &amp; coupons.<br><br><span style="color:#fff">Mailpost for PressKit error:</span> There is no form with ID 0, perhaps it was deleted?<br><br>By subscribing you accepted the our <u>Policy</u></div>
    <div class="abs" style="left:202px;top:262px;width:570px;height:1px;background:#222"></div>
    <div class="abs" style="left:0;width:974px;text-align:center;top:278px;font-size:6px;color:#9aa0aa">© 2024 Copyright by Tavi Linkway Africa.</div>
    <div class="abs" style="left:946px;top:290px;width:18px;height:18px;border-radius:50%;border:1px solid var(--green)"></div>
  </footer>
</div>
</body>
</html>
```